Labeling for Organic Food

we need a label design for

1. Organic Red Rice
2. Organic wild honey

it is going to be the same design in different dimensions.

1. Organic Red Rice
Dimension 1 28*18.5cm
Dimension 2 13.5*8cm

2. Organic Honey
12*6cm
Updates

There is an update in the brief about using the Bhutanese color scheme. Please check it out.

Target Market(s)

people with the concern of health and the environment.

Requirements
Must have
• 1. our logo
• 2. All the info
• 3. A natural feel
• 4. I would prefer minimalistic style
• 5. Please include Bhutanese national colours as attached.

```html
<!DOCTYPE html>
<html lang="en">
<head>
<meta charset="UTF-8">
<title>Organic Wild Honey Label</title>
<link href="https://fonts.googleapis.com/css2?family=Oswald:wght@400;500;600&family=Noto+Serif+SC:wght@300&display=swap" rel="stylesheet">
<style>
  :root {
    --page-bg: #efefef;
    --label-yellow: #ffe25c;
    --label-black: #111111;
    --gold: #f9dc55;
    --ink: #151515;
  }
  * { margin: 0; padding: 0; box-sizing: border-box; }
  html, body {
    width: 1200px;
    height: 800px;
    overflow: hidden;
    background: var(--page-bg);
  }
  .canvas {
    position: relative;
    width: 1200px;
    height: 800px;
  }
  .label {
    position: absolute;
    left: 57px;
    top: 169px;
    width: 1086px;
    height: 462px;
    font-family: 'Oswald', sans-serif;
  }
  .label-band {
    position: absolute;
    left: 0;
    top: 92px;
    width: 1086px;
    height: 291px;
    background: var(--label-yellow);
  }
  .label-hexagon {
    position: absolute;
    left: 0;
    top: 0;
    width: 1086px;
    height: 462px;
  }
  .label-hexagon polygon { fill: var(--label-black); }

  .info-panel {
    position: absolute;
    color: var(--ink);
    text-align: center;
    text-transform: uppercase;
    font-weight: 500;
  }
  .info-panel--left {
    left: 24px;
    top: 121px;
    width: 240px;
    font-size: 15.5px;
    line-height: 1.22;
  }
  .info-panel--left p { margin-bottom: 19px; }
  .info-panel--right {
    left: 812px;
    top: 117px;
    width: 254px;
    font-size: 14px;
    line-height: 1.4;
    letter-spacing: 0.6px;
  }

  .front-panel {
    position: absolute;
    left: 280px;
    top: 0;
    width: 530px;
    height: 462px;
    text-align: center;
    color: var(--gold);
    text-transform: uppercase;
  }
  .brand-name {
    position: absolute;
    left: 0;
    top: 82px;
    width: 100%;
    font-size: 28px;
    font-weight: 500;
    letter-spacing: 3px;
  }
  .product-name {
    position: absolute;
    left: 0;
    top: 184px;
    width: 100%;
    font-size: 55px;
    font-weight: 500;
    line-height: 1.2;
    transform: scaleX(0.9);
  }
  .product-name-zh {
    position: absolute;
    left: 0;
    top: 253px;
    width: 100%;
    font-family: 'Noto Serif SC', serif;
    font-weight: 300;
    font-size: 45px;
    line-height: 1.2;
  }
  .origin {
    position: absolute;
    left: 0;
    top: 327px;
    width: 100%;
    font-size: 30px;
    font-weight: 500;
    transform: scaleX(0.88);
  }
  .net-weight {
    position: absolute;
    left: 0;
    top: 403px;
    width: 100%;
    font-size: 23px;
    font-weight: 500;
    transform: scaleX(0.88);
  }
</style>
</head>
<body>
<main class="canvas">
  <section class="label">
    <div class="label-band"></div>
    <svg class="label-hexagon" viewBox="0 0 1086 462" aria-hidden="true">
      <polygon points="280,231 403,0 677,0 810,231 678,462 402,462"/>
    </svg>

    <div class="info-panel info-panel--left">
      <p>Store in a cool and dry place</p>
      <p>Ingredients: organic Bhutanese<br>wild honey</p>
      <p>Best before 31/12/19</p>
      <p>Product of Bhutan</p>
      <p>Distributed by Greenfield Provisions<br>42 Meadow Lane Singapore<br>600123</p>
    </div>

    <div class="front-panel">
      <div class="brand-name">Dzong Hive</div>
      <h1 class="product-name">Organic Wild Honey</h1>
      <div class="product-name-zh">有机野生蜂蜜</div>
      <div class="origin">Product of Bhutan</div>
      <div class="net-weight">Net weight 250ml</div>
    </div>

    <div class="info-panel info-panel--right">
      Organic wild honey is freshly collected from the remote unpolluted lands of the Himalayans in Bhutan. The bees are not fed sugar and antibiotics and the honey is free from chemical preservatives, coloring and additives. The wild honey is not heat treated and unprocessed to retain the optimum level of nutritional value and enzymes
    </div>
  </section>
</main>
</body>
</html>
```